Northfield Builders Guild Business card

We are looking for a new business card design with photo included.
Our business is a nonprofit construction contractor membership organization. We offer business education, assist with business setup and licensing, provide safety training, and provide a member directory.
URL: www.brickwayguildnetwork.org
Color code:
CMYK: 0 cyan, 42 magenta, 100 yellow, 0 black for Print.
Hexidecimal: #FF9900
RGB: R 255; G 153; B 0

```html
<!DOCTYPE html>
<html lang="en">
<head>
<meta charset="utf-8">
<title>Northfield Builders Guild – Business Card</title>
<link href="https://fonts.googleapis.com/css2?family=Arimo:wght@400;700&display=swap" rel="stylesheet">
<style>
  :root {
    --backdrop: #e4e4e2;
    --card: #2b2b2b;
    --card-edge: #b86f0a;
    --orange: #ff9900;
    --white: #f2f2f2;
    --muted: #d9d9d9;
    --rule: #8a8a8a;
  }
  * { margin: 0; padding: 0; box-sizing: border-box; }
  html, body {
    width: 1200px; height: 801px; overflow: hidden;
    background: var(--backdrop);
    font-family: "Arimo", Arial, sans-serif;
  }
  .sheet {
    position: relative; width: 1200px; height: 801px;
    display: flex; align-items: center; justify-content: center; gap: 40px;
  }
  .card {
    position: relative; width: 540px; height: 309px;
    background: var(--card);
    border-bottom: 3px solid var(--card-edge);
    box-shadow: 0 10px 24px rgba(0,0,0,0.18);
    overflow: hidden;
  }
  /* back side: contact details */
  .card-back .wordmark {
    position: absolute; left: 36px; top: 168px; width: 220px;
    font-weight: 700; font-size: 19px; line-height: 1.15;
    color: var(--white); text-transform: uppercase; letter-spacing: 0.5px;
  }
  .card-back .divider {
    position: absolute; left: 275px; top: 40px; width: 1px; height: 230px;
    background: var(--rule);
  }
  .contact {
    position: absolute; left: 296px; top: 40px; width: 230px;
    color: var(--white);
  }
  .contact .person { font-weight: 700; font-size: 22px; color: var(--orange); line-height: 1.1; }
  .contact .role { font-size: 14px; color: var(--muted); margin-top: 4px; }
  .contact .address { font-size: 14px; color: var(--muted); margin-top: 18px; line-height: 1.35; }
  .contact .lines { list-style: none; margin-top: 16px; }
  .contact .lines li {
    display: flex; align-items: center; gap: 8px;
    font-size: 13.5px; color: var(--muted); margin-bottom: 8px; white-space: nowrap;
  }
  .contact .icon { width: 14px; height: 14px; flex: none; }
  /* front side: name */
  .card-front .wordmark {
    position: absolute; left: 0; right: 0; top: 92px;
    text-align: center;
    font-weight: 700; font-size: 44px; line-height: 1.1;
    color: var(--orange); text-transform: uppercase; letter-spacing: 1px;
  }
</style>
</head>
<body>
<main class="sheet">
  <section class="card card-back" aria-label="Card back">
    <div class="wordmark">Northfield Builders Guild</div>
    <div class="divider"></div>
    <div class="contact">
      <p class="person">Daniel Hartley</p>
      <p class="role">Manager</p>
      <p class="address">Your address, city<br>state, ZIP 0000</p>
      <ul class="lines">
        <li>
          <svg class="icon" viewBox="0 0 16 16" aria-hidden="true"><path fill="#ff9900" d="M3.5 1.5l2.5 0 1 3.5-1.6 1.1a8 8 0 0 0 4.5 4.5L11 9l3.5 1v2.5c0 1-1 2-2 2A11 11 0 0 1 1.5 3.5c0-1 1-2 2-2z"/></svg>
          555-014-2100
        </li>
        <li>
          <svg class="icon" viewBox="0 0 16 16" aria-hidden="true"><rect x="1" y="3" width="14" height="10" fill="#ff9900"/><path d="M1 3l7 6 7-6" fill="none" stroke="#2b2b2b" stroke-width="1.4"/></svg>
          info@brickwayguildnetwork.org
        </li>
        <li>
          <svg class="icon" viewBox="0 0 16 16" aria-hidden="true"><circle cx="8" cy="8" r="6.5" fill="none" stroke="#ff9900" stroke-width="1.6"/><ellipse cx="8" cy="8" rx="2.6" ry="6.5" fill="none" stroke="#ff9900" stroke-width="1.3"/><path d="M1.5 8h13" stroke="#ff9900" stroke-width="1.3"/></svg>
          www.brickwayguildnetwork.org
        </li>
      </ul>
    </div>
  </section>

  <section class="card card-front" aria-label="Card front">
    <div class="wordmark">Northfield<br>Builders Guild</div>
  </section>
</main>
</body>
</html>
```